WordPress Design - dental products

We need a Wordpress theme for a company based in Mexico, USA and Europe. We sell orthodontic products for dental industry. We are very compromised with our customers and all our products are the better option in the market. The Quality and image are really important for us.

The idea is to have a Wordpress Website that we can manage, and our customers can get info from us. Our corporate image is based in innovation, quality and customer service.

the general idea is to have a wordpress site to manage all the info and the store is in a different system, so that we need is the wordpress site desing for the frontend. 

We will need more designs so in the future for our website, so the winner will help us for many projects.

So we hope the best design.
Updates

Hi, this "wordpress site" will be used as a homepage, the eCommerce is independent. So the design is related to corporate site. Thank you

Target Market(s)

Target: dental and orthodontic industry, academy and general customers. Private an public organizations related to medical and dental industry.
Investigators and press

Industry/Entity Type

Dental

Requirements
Must have
• Must Have Priorities:
• - Respect the logo (included)
• - Respect colors (actual website)
• - Modern style and innovated website
Nice to have
• Be funcionality, simply and easy to use, think about user interfaze (UI)
Should not have
• The design should not use old-style, serif fonts like Times New Roman. Not use cartoons, flash animations, free icons. Don't modify the logo.

```html
<!DOCTYPE html>
<html lang="es">
<head>
<meta charset="utf-8">
<title>Orto-Vela — Todo en ortodoncia</title>
<link rel="stylesheet" href="https://fonts.googleapis.com/css2?family=Gelasio:wght@400&family=Arimo:wght@400;700&display=swap">
<style>
:root{
  --red-dark:#6e0a16;
  --red:#9a1320;
  --red-mid:#b3202c;
  --footer:#94141b;
  --footer-box:#7a0d14;
  --paper:#ffffff;
  --ink:#3c3c3c;
  --rule:#e6e6e6;
}
*{box-sizing:border-box;margin:0;padding:0}
html,body{width:900px;height:1200px;overflow:hidden}
body{position:relative;background:#fff;font-family:"Arimo",Arial,sans-serif;color:var(--ink)}
h1,h2,h3,h4{font-weight:400}
.backdrop{position:absolute;left:0;top:0;width:900px;height:1200px}
.abs{position:absolute}

/* header */
.brand{left:107px;top:12px;display:flex;align-items:center;gap:10px}
.brand-mark{width:48px;height:70px;border:2px solid #e0b9a0}
.brand-name{font-family:"Arimo",Arial,sans-serif;font-weight:700;font-size:24px;color:#fff;line-height:1}
.brand-tag{display:block;font-size:9px;color:#fff;margin-top:4px;letter-spacing:.5px}
.login{left:425px;top:0;width:384px;height:36px;background:var(--red);border:1px solid #5e0912;border-top:none;border-radius:0 0 5px 5px;box-shadow:0 2px 4px rgba(0,0,0,.35);display:flex;align-items:center;gap:9px;padding:0 10px}
.field{height:18px;background:#fff;border-radius:3px;font-size:10px;color:#9a9a9a;padding:3px 7px}
.btn-small{height:20px;padding:0 12px;background:var(--red-mid);border:1px solid #5e0912;border-radius:3px;color:#fff;font-size:10px;font-weight:700;line-height:18px}

.nav{left:107px;top:94px;width:702px;height:34px;background:linear-gradient(#b71f2a,#93111c);border-radius:4px;box-shadow:0 2px 5px rgba(0,0,0,.35);display:flex;align-items:center;padding:0 6px}
.nav-item{height:22px;padding:0 11px;margin-right:8px;border:1px solid #5e0912;background:linear-gradient(#b31d28,#8d0f19);border-radius:2px;color:#fff;font-size:10px;line-height:20px;white-space:nowrap}
.search{margin-left:auto;display:flex;align-items:center;gap:6px}
.search-box{width:163px;height:21px;background:#fff;border-radius:11px;display:flex;align-items:center;padding-left:8px}
.search-label{color:#fff;font-size:9.5px;font-weight:700;margin-right:8px}

/* hero */
.hero{left:106px;top:139px;width:703px;height:231px;background:linear-gradient(#ffffff,#e2e2e2);box-shadow:0 3px 8px rgba(0,0,0,.25)}
.hero-title{left:45px;top:24px;font-family:"Gelasio",Georgia,serif;font-size:37px;color:var(--red);line-height:1.2}
.hero-text{left:46px;top:83px;width:340px;font-family:"Gelasio",Georgia,serif;font-size:14px;line-height:22.5px;color:#6a6a6a}
.hero-btn{left:47px;top:185px;width:126px;height:30px;background:linear-gradient(#c3363d,#8f141c);border-radius:4px;color:#fff;font-family:"Gelasio",Georgia,serif;font-size:13px;text-align:center;line-height:29px;box-shadow:0 1px 2px rgba(0,0,0,.4)}
.hero-photo{left:449px;top:0;width:254px;height:231px;background:radial-gradient(ellipse at 60% 45%,#f4d6c4 0%,#e5a88f 45%,#f3d9c9 80%)}

/* content */
.page{left:106px;top:370px;width:703px;height:606px;background:var(--paper)}
.post-title{left:97px;width:487px;height:39px;background:linear-gradient(#a8161f,#8a0f18);color:#fff;font-family:"Gelasio",Georgia,serif;font-size:17.5px;line-height:21px;padding:9px 23px;box-shadow:0 2px 4px rgba(0,0,0,.3);white-space:nowrap}
.post-meta{left:123px;font-family:"Gelasio",Georgia,serif;font-size:8px;letter-spacing:.8px;color:#666;display:flex;align-items:center;gap:6px;white-space:nowrap}
.post-meta .comments{display:flex;align-items:center;gap:6px;margin-left:10px}
.post-body{left:123px;width:449px;font-size:10px;line-height:18px;color:#3c3c3c;hyphens:manual}
.read-more{left:521px;font-family:"Gelasio",Georgia,serif;font-size:9.5px;color:#444;text-decoration:underline;white-space:nowrap}
.post-rule{left:123px;width:449px;height:1px;background:var(--rule)}
.next-page{left:487px;top:950px;font-family:"Gelasio",Georgia,serif;font-size:9.5px;color:#444;text-decoration:underline;white-space:nowrap}

.side-title{left:617px;font-family:"Gelasio",Georgia,serif;font-size:13.5px;color:var(--red);white-space:nowrap}
.side-rule{left:609px;width:188px;height:1px;background:var(--rule)}
.thumb{width:56px;height:58px;border:1px solid #d4d4d4;background:#fff;padding:3px;box-shadow:0 1px 2px rgba(0,0,0,.12)}
.thumb span{display:block;width:100%;height:100%;background:radial-gradient(ellipse at 50% 55%,#f6efe8 0 22%,#c86e58 40%,#e3a486 80%)}
.latest{left:611px;top:697px;width:186px;list-style:none}
.latest li{height:20px;border-bottom:1px solid #ededed;font-size:10px;color:#555;display:flex;align-items:center;gap:8px}
.latest li::before{content:"";width:9px;height:9px;border-radius:50%;background:var(--red)}

/* footer */
.footer{left:101px;top:976px;width:714px;height:158px;background:var(--footer);box-shadow:0 3px 6px rgba(0,0,0,.3);color:#fff}
.foot-title{font-family:"Gelasio",Georgia,serif;font-size:13px;color:#fff;white-space:nowrap;line-height:18px}
.tweets{left:12px;top:47px;width:285px;height:48px;background:var(--footer-box);border-radius:3px;padding:6px 7px;font-family:"Gelasio",Georgia,serif;font-size:10px;line-height:14px}
.social{width:23px;height:23px;border-radius:3px;background:#f1e4e4}
.divider{top:22px;width:1px;height:110px;background:#6e0b12}
.mail{left:339px;top:49px;width:173px;height:25px;background:#fff;border:1px solid #6e0b12;color:#555;font-size:11px;padding:5px 8px}
.subscribe{left:375px;top:84px;width:92px;height:24px;background:linear-gradient(#c0343b,#8c1018);border:1px solid #6e0b12;border-radius:3px;font-family:"Gelasio",Georgia,serif;font-size:13px;text-align:center;line-height:22px}
.legal{left:546px;top:46px;font-family:"Gelasio",Georgia,serif;font-size:10.5px;line-height:18px;white-space:nowrap}
</style>
</head>
<body>

<svg class="backdrop" viewBox="0 0 900 1200" aria-hidden="true">
  <defs>
    <linearGradient id="bgRed" x1="0" y1="0" x2="0" y2="1">
      <stop offset="0" stop-color="#7d0e1b"/>
      <stop offset="1" stop-color="#a3151f"/>
    </linearGradient>
    <linearGradient id="bgGrey" x1="0" y1="0" x2="0" y2="1">
      <stop offset="0" stop-color="#e4e4e4"/>
      <stop offset="1" stop-color="#ffffff"/>
    </linearGradient>
  </defs>
  <rect width="900" height="1200" fill="#fff"/>
  <rect width="900" height="520" fill="url(#bgRed)"/>
  <path d="M0 250 C150 300 300 420 450 520 L0 520 Z" fill="url(#bgGrey)"/>
  <path d="M0 160 C200 260 360 420 380 700 L0 700 Z" fill="#f1f1f1" opacity=".9"/>
  <path d="M0 300 C120 380 230 450 300 700 L0 700 Z" fill="#fafafa"/>
  <path d="M450 110 C620 170 780 150 900 120 L900 520 L450 520 Z" fill="url(#bgGrey)"/>
  <path d="M520 60 C650 110 800 80 900 30 L900 90 C790 140 650 150 520 60 Z" fill="#c11f2a" opacity=".6"/>
  <path d="M0 60 C80 120 120 220 110 330" stroke="#c7232d" stroke-width="30" fill="none" opacity=".5"/>
  <rect y="520" width="900" height="680" fill="#fff"/>
</svg>

<header>
  <div class="abs brand">
    <div class="brand-mark"></div>
    <div>
      <span class="brand-name">Orto-Vela</span>
      <span class="brand-tag">TODO EN ORTODONCIA...</span>
    </div>
  </div>

  <form class="abs login">
    <div class="field" style="width:143px">e-Mail</div>
    <div class="field" style="width:143px">Contraseña</div>
    <div class="btn-small">Iniciar</div>
  </form>

  <nav class="abs nav">
    <span class="nav-item">Inicio</span>
    <span class="nav-item">Acerda de</span>
    <span class="nav-item">Servicios</span>
    <span class="nav-item">Galeria</span>
    <span class="nav-item">Eventos</span>
    <div class="search">
      <div class="search-box">
        <svg width="10" height="10" viewBox="0 0 10 10" aria-hidden="true"><circle cx="4" cy="4" r="3" stroke="#555" stroke-width="1.5" fill="none"/><path d="M6.3 6.3 9 9" stroke="#555" stroke-width="1.6"/></svg>
      </div>
      <span class="search-label">Buscar</span>
    </div>
  </nav>
</header>

<div class="abs page"></div>

<section class="abs hero">
  <h1 class="abs hero-title">Bienvenido</h1>
  <p class="abs hero-text">Lorem ipsum dolor sit amet, consectetur adipiscing elit. Donec rutrum risus quis erat sagittis quis vehicula magna hendrerit. Suspendisse non lectus sit amet dolor eleifend accumsan.</p>
  <div class="abs hero-btn">conocenos</div>
  <div class="abs hero-photo" role="img" aria-label="Fotografía de una sonrisa con dientes blancos"></div>
</section>

<main>
  <h2 class="abs post-title" style="top:414px">Este titulo es de muestra, solo para este post.</h2>
  <div class="abs post-meta" style="top:468px">
    <svg width="9" height="9" viewBox="0 0 9 9" aria-hidden="true"><rect x=".5" y="1" width="8" height="7.5" fill="#fff" stroke="#b33"/><rect x=".5" y="1" width="8" height="2" fill="#c33"/></svg>
    8 DE OCTUBRE DE 2010
    <span class="comments"><svg width="10" height="9" viewBox="0 0 10 9" aria-hidden="true"><path d="M1 1h8v5H4L2 8V6H1z" fill="none" stroke="#aaa"/></svg><u>3 COMENTARIOS</u></span>
  </div>
  <p class="abs post-body" style="top:489px">Lorem ipsum dolor sit amet, consectetur adipiscing elit. Quisque laoreet faucibus hendrerit. Ut sol&shy;licitudin gravida leo, et pretium felis tempor vel. Nulla at odio et nisl luctus tristique. In dolor enim, molestie sit amet tempus eget, lobortis eget sapien. Etiam ut elit et velit scelerisque scelerisque. Pellentesque venenatis pulvinar urna at dignissim. Nulla ac urna sapien. Nulla tempus velit nec magna sollicitudin consequat. Duis sem mauris, gravida ac vehicula eget, tincidunt a est. Cras pel&shy;lentesque, magna sit amet dapibus varius, mauris tortor volutpat turpis, a ornare risus lacus in augue. Mauris vel risus sit amet lorem pellentesque consequat in a est. Morbi vel libero nisi. Curabi&shy;tur in justo turpis, vitae vehicula lacus.</p>
  <a class="abs read-more" style="top:634px">leer mas »</a>
  <div class="abs post-rule" style="top:661px"></div>

  <h2 class="abs post-title" style="top:685px">Este titulo es de muestra, solo para este post.</h2>
  <div class="abs post-meta" style="top:739px">
    <svg width="9" height="9" viewBox="0 0 9 9" aria-hidden="true"><rect x=".5" y="1" width="8" height="7.5" fill="#fff" stroke="#b33"/><rect x=".5" y="1" width="8" height="2" fill="#c33"/></svg>
    8 DE OCTUBRE DE 2010
    <span class="comments"><svg width="10" height="9" viewBox="0 0 10 9" aria-hidden="true"><path d="M1 1h8v5H4L2 8V6H1z" fill="none" stroke="#aaa"/></svg><u>3 COMENTARIOS</u></span>
  </div>
  <p class="abs post-body" style="top:759px">Lorem ipsum dolor sit amet, consectetur adipiscing elit. Quisque laoreet faucibus hendrerit. Ut sol&shy;licitudin gravida leo, et pretium felis tempor vel. Nulla at odio et nisl luctus tristique. In dolor enim, molestie sit amet tempus eget, lobortis eget sapien. Etiam ut elit et velit scelerisque scelerisque. Pellentesque venenatis pulvinar urna at dignissim. Nulla ac urna sapien. Nulla tempus velit nec magna sollicitudin consequat. Duis sem mauris, gravida ac vehicula eget, tincidunt a est. Cras pel&shy;lentesque, magna sit amet dapibus varius, mauris tortor volutpat turpis, a ornare risus lacus in augue. Mauris vel risus sit amet lorem pellentesque consequat in a est. Morbi vel libero nisi. Curabi&shy;tur in justo turpis, vitae vehicula lacus.</p>
  <a class="abs read-more" style="top:905px">leer mas »</a>
  <div class="abs post-rule" style="top:932px"></div>
  <a class="abs next-page">Página siguiente »</a>
</main>

<aside>
  <h3 class="abs side-title" style="top:421px">galeria de fotos</h3>
  <div class="abs side-rule" style="top:442px"></div>
  <div class="abs thumb" style="left:609px;top:454px" role="img" aria-label="Foto de sonrisa"><span></span></div>
  <div class="abs thumb" style="left:674px;top:454px" role="img" aria-label="Foto de sonrisa"><span></span></div>
  <div class="abs thumb" style="left:739px;top:454px" role="img" aria-label="Foto de sonrisa"><span></span></div>
  <div class="abs thumb" style="left:609px;top:522px" role="img" aria-label="Foto de sonrisa"><span></span></div>
  <div class="abs thumb" style="left:674px;top:522px" role="img" aria-label="Foto de sonrisa"><span></span></div>
  <div class="abs thumb" style="left:739px;top:522px" role="img" aria-label="Foto de sonrisa"><span></span></div>
  <div class="abs thumb" style="left:609px;top:590px" role="img" aria-label="Foto de sonrisa"><span></span></div>
  <div class="abs thumb" style="left:674px;top:590px" role="img" aria-label="Foto de sonrisa"><span></span></div>
  <div class="abs thumb" style="left:739px;top:590px" role="img" aria-label="Foto de sonrisa"><span></span></div>

  <h3 class="abs side-title" style="top:669px">ultimos posts</h3>
  <div class="abs side-rule" style="top:689px"></div>
  <ul class="abs latest">
    <li>Lorem ipsum dolor sit ament</li>
    <li>Lorem ipsum dolor sit ament</li>
    <li>Lorem ipsum dolor sit ament</li>
    <li>Lorem ipsum dolor sit ament</li>
    <li>Lorem ipsum dolor sit ament</li>
  </ul>
</aside>

<footer class="abs footer">
  <h4 class="abs foot-title" style="left:125px;top:14px">Tweets Recientes</h4>
  <div class="abs tweets">@usuario: Hola, gracias por mantenerte en contacto<br>@curioso: Exactamente a eso se refiere, saludos.</div>
  <div class="abs social" style="left:13px;top:115px"></div>
  <div class="abs social" style="left:47px;top:115px"></div>
  <div class="abs social" style="left:82px;top:115px"></div>
  <div class="abs social" style="left:115px;top:115px"></div>
  <span class="abs foot-title" style="left:165px;top:118px">Redes Sociales</span>

  <div class="abs divider" style="left:323px"></div>
  <h4 class="abs foot-title" style="left:347px;top:14px">Suscribete a nuestro boletin</h4>
  <div class="abs mail">Introduce tu e-Mail..</div>
  <div class="abs subscribe">Suscribete</div>

  <div class="abs divider" style="left:533px"></div>
  <p class="abs legal">Copyright © 2010 Ortovela<br>All rights reserved<br>Tel: 52+ (55) 10203040</p>
</footer>

</body>
</html>
```